Harborline Self Storage

looking for a clean sharp easy to read advertising billboard to rent units

online rentals
online payment
online check out

climate control units available
competitive rates

https://www.harborline-selfstorage.example/

```html
<!DOCTYPE html>
<html lang="en">
<head>
<meta charset="utf-8">
<title>Harborline Self Storage — Billboard</title>
<link rel="stylesheet" href="https://fonts.googleapis.com/css2?family=Krona+One&family=Montserrat:wght@600;800&display=swap">
<style>
  :root {
    --navy: #1d2366;
    --red: #ee2a2f;
    --white: #ffffff;
    --page: #ffffff;
    --door-blue: #1f3fa8;
    --door-deep: #142c7c;
    --corridor: #c9ccd4;
  }
  html, body {
    margin: 0;
    width: 1200px;
    height: 1112px;
    overflow: hidden;
    background: var(--page);
  }
  .billboard {
    position: absolute;
    left: 20px;
    top: 343px;
    width: 1160px;
    height: 425px;
    box-shadow: 0 6px 16px rgba(0, 0, 0, 0.18);
  }
  .brand-name, .feature {
    font-family: "Krona One", sans-serif;
    fill: var(--navy);
  }
  .perk {
    font-family: "Montserrat", sans-serif;
    font-weight: 800;
    fill: var(--white);
  }
  .phone-number {
    font-family: "Krona One", sans-serif;
    fill: var(--white);
  }
  .web-address {
    font-family: "Montserrat", sans-serif;
    font-weight: 600;
    fill: var(--white);
  }
  .web-address .tld { fill: var(--red); }
</style>
</head>
<body>
<svg class="billboard" viewBox="0 0 1160 425" xmlns="http://www.w3.org/2000/svg">
  <defs>
    <linearGradient id="corridor-tones" x1="0" y1="0" x2="1" y2="0">
      <stop offset="0" stop-color="var(--door-deep)"/>
      <stop offset="0.25" stop-color="var(--door-blue)"/>
      <stop offset="0.5" stop-color="var(--corridor)"/>
      <stop offset="0.75" stop-color="var(--door-blue)"/>
      <stop offset="1" stop-color="var(--door-deep)"/>
    </linearGradient>
  </defs>

  <rect class="board-bg" width="1160" height="425" fill="var(--white)"/>

  <!-- storage corridor photo area -->
  <polygon class="photo-area" role="img" aria-label="Photo of an indoor storage corridor lined with blue roll-up unit doors"
           points="623,0 1160,0 1160,359 795,359" fill="url(#corridor-tones)"/>

  <!-- diagonal red stripe -->
  <polygon class="accent-stripe" points="562,0 604,0 775,359 733,359" fill="var(--red)"/>

  <!-- brand name -->
  <rect class="brand-mark" x="20" y="28" width="40" height="40" fill="var(--red)"/>
  <text class="brand-name" x="74" y="60" font-size="34" textLength="420" lengthAdjust="spacingAndGlyphs">HARBORLINE</text>
  <text class="brand-name" x="74" y="100" font-size="34" textLength="420" lengthAdjust="spacingAndGlyphs">SELF STORAGE</text>

  <!-- feature list -->
  <g class="feature-list">
    <polygon points="0,140 34,140 43,164 0,164" fill="var(--red)"/>
    <text class="feature" x="53" y="164" font-size="32" textLength="481" lengthAdjust="spacingAndGlyphs">ONLINE RENTALS</text>
    <polygon points="0,182 34,182 43,206 0,206" fill="var(--red)"/>
    <text class="feature" x="53" y="206" font-size="32" textLength="508" lengthAdjust="spacingAndGlyphs">ONLINE PAYMENT</text>
    <polygon points="0,224 34,224 43,249 0,249" fill="var(--red)"/>
    <text class="feature" x="53" y="249" font-size="32" textLength="546" lengthAdjust="spacingAndGlyphs">ONLINE CHECK OUT</text>
  </g>

  <!-- perks band -->
  <polygon class="perks-band" points="0,271 678,271 721,356 0,356" fill="var(--red)"/>
  <g class="perks">
    <text class="perk" x="11" y="310" font-size="30">★</text>
    <text class="perk" x="42" y="310" font-size="32" textLength="338" lengthAdjust="spacingAndGlyphs">CLIMATE CONTROL</text>
    <text class="perk" x="42" y="341" font-size="32" textLength="315" lengthAdjust="spacingAndGlyphs">UNITS AVAILABLE</text>
    <text class="perk" x="395" y="310" font-size="30">★</text>
    <text class="perk" x="427" y="310" font-size="32" textLength="241" lengthAdjust="spacingAndGlyphs">COMPETITIVE</text>
    <text class="perk" x="427" y="341" font-size="32" textLength="114" lengthAdjust="spacingAndGlyphs">RATES</text>
  </g>

  <!-- contact bar -->
  <rect class="contact-bar" x="0" y="361" width="1160" height="64" fill="var(--navy)"/>
  <polygon class="contact-divider" points="595,361 608,361 647,425 634,425" fill="var(--white)"/>

  <g class="phone-icon" transform="translate(14,372) scale(1.6)" fill="var(--red)">
    <path d="M6.6 10.8c1.4 2.8 3.8 5.1 6.6 6.6l2.2-2.2c.3-.3.7-.4 1-.2 1.1.4 2.3.6 3.6.6.6 0 1 .4 1 1V20c0 .6-.4 1-1 1C10.6 21 3 13.4 3 4c0-.6.4-1 1-1h3.5c.6 0 1 .4 1 1 0 1.3.2 2.5.6 3.6.1.3 0 .7-.2 1z"/>
  </g>
  <text class="phone-number" x="58" y="412" font-size="44" textLength="526" lengthAdjust="spacingAndGlyphs">555-013-4000</text>

  <g class="globe-icon" fill="none" stroke="var(--red)" stroke-width="2">
    <circle cx="667" cy="394" r="13"/>
    <ellipse cx="667" cy="394" rx="6" ry="13"/>
    <line x1="654" y1="394" x2="680" y2="394"/>
    <line x1="656" y1="387" x2="678" y2="387"/>
    <line x1="656" y1="401" x2="678" y2="401"/>
  </g>
  <text class="web-address" x="690" y="406" font-size="32" textLength="447" lengthAdjust="spacingAndGlyphs">harborline-selfstorage<tspan class="tld">.example</tspan></text>
</svg>
</body>
</html>
```